BVA Early College and Career Program

Starting a new program initiative at Birchvale High School where students will have the opportunity to take college courses during their senior year of high school. Preferably add some pictures to reflect the career pathways we are offering (below) Some context to use for this flyer are:

Learn more about the career focused courses in…
• Education
• Computer & Information Science
• Technology & Engineering
• Health

Things to look forward to:
Experience college in high school
Finish college early
Save money on college tuition and fees
Advice on Career pathways

all classes fit into OPEN CREDIT PATHWAY

For more information contact

Peter Hollis - PK12 Partnerships -RWTC
555.204.3189
Email: phollis@rwtc.example.edu

Ms. Delgany- Early College Coordinator
Email: marta.delgany@birchvale.example.org
Room K215

I uploaded 5 or so photos that I would like to see incorporated in the design of the flier- using real students from our high school will give a more realistic approach- thanks, Added Monday, August 21, 2017

Target Market(s)

High school students who are currently in 10th grade (for recruitment) and only high school juniors and seniors are able to apply.

Industry/Entity Type

School

Colors

Designer to choose colors to be used in the design.

Requirements
Must have
• logos- some pictures reflecting the different career pathways and the contact information provided. Looking to also have this in a format that I can print on card stock paper not just full length page- ADD / USE photos attached to see which one fits the project better.
Nice to have
• suitable for high school students- attractive
Should not have
• Do not include any generic phone numbers.

```html
<!DOCTYPE html>
<html lang="en">
<head>
<meta charset="utf-8">
<title>BVA Early College Program</title>
<link href="https://fonts.googleapis.com/css2?family=Source+Sans+3:wght@400;600;700&display=swap" rel="stylesheet">
<style>
  :root{
    --navy:#1b3a6b;
    --navy-deep:#173463;
    --blue:#4a86c8;
    --blue-light:#5b93d1;
    --ring:#d3d6db;
    --grey:#c9c9c9;
    --text-grey:#6d6f73;
    --white:#ffffff;
  }
  *{box-sizing:border-box;margin:0;padding:0}
  html,body{width:970px;height:1200px;overflow:hidden;background:#fff}
  body{font-family:"Source Sans 3",sans-serif}
  .flyer{position:relative;width:970px;height:1200px;overflow:hidden;background:var(--white)}
  .flyer-shapes{position:absolute;inset:0}
  .abs{position:absolute}

  .brand-row{top:72px;right:16px;display:flex;gap:22px;align-items:center}
  .brand{display:flex;align-items:center;gap:8px;color:var(--navy);font-weight:600;font-size:20px;line-height:1.05}
  .brand-mark{width:16px;height:16px;background:var(--navy);flex:none}

  .program-title{left:380px;width:678px;top:226px;width:590px;text-align:center;color:var(--white);font-weight:600;font-size:37px;line-height:49px}
  .program-lead{left:560px;width:400px;top:374px;transform:translateX(-0px);text-align:center;color:var(--navy);font-weight:600;font-size:21.5px;line-height:28px}

  .perks{left:34px;top:527px}
  .perks h2{font-size:19px;font-weight:700;color:var(--navy);letter-spacing:.1px;margin-bottom:4px}
  .perks ul{list-style:none}
  .perks li{position:relative;padding-left:24px;font-size:19.5px;color:var(--text-grey);line-height:29.5px}
  .perks li::before{content:"";position:absolute;left:2px;top:9px;width:13px;height:13px;border-radius:50%;background:var(--blue)}
  .perks li::after{content:"";position:absolute;left:6px;top:13px;width:4px;height:4px;border-top:2px solid #fff;border-right:2px solid #fff;transform:rotate(45deg)}

  .pathway-label{color:var(--white);font-weight:600;font-size:19px;line-height:26px;text-align:center;width:240px;transform:translateX(-50%)}

  .cta-text{left:560px;width:410px;top:914px;text-align:center;color:var(--white);font-size:19px;letter-spacing:.2px}

  .contact{top:1007px;color:var(--white)}
  .contact h3{font-size:21px;font-weight:600;margin-bottom:4px}
  .contact p{font-size:17px;line-height:26px;color:#e4eaf3;display:flex;align-items:center;gap:8px;white-space:nowrap}
  .contact .mail{font-size:16px;letter-spacing:-.3px}
  .contact svg{flex:none}
</style>
</head>
<body>
<main class="flyer">
  <svg class="flyer-shapes" width="970" height="1200" viewBox="0 0 970 1200" aria-hidden="false">
    <defs>
      <linearGradient id="photoTone" x1="0" y1="0" x2="1" y2="1">
        <stop offset="0" stop-color="#d9cfc6"/>
        <stop offset=".45" stop-color="#b89a8a"/>
        <stop offset=".75" stop-color="#8e6aa6"/>
        <stop offset="1" stop-color="#c9ccd4"/>
      </linearGradient>
    </defs>

    <!-- title band -->
    <rect class="title-band" x="380" y="200" width="590" height="147" fill="var(--navy)"/>
    <rect x="380" y="200" width="590" height="6" fill="var(--blue)"/>
    <rect x="380" y="341" width="590" height="6" fill="var(--blue)"/>

    <!-- hero photo area -->
    <g role="img" aria-label="Photo of a smiling student holding a red book in a library">
      <polygon points="0,0 285,0 536,504 0,504" fill="url(#photoTone)"/>
    </g>
    <polygon class="hero-stripe" points="285,0 331,0 612,504 548,504" fill="var(--blue)"/>
    <polygon class="hero-edge" points="331,0 342,0 630,504 612,504" fill="var(--grey)"/>

    <!-- lower navy field -->
    <polygon points="0,800 970,500 970,516 0,864" fill="var(--blue-light)"/>
    <polygon points="0,864 970,516 970,1158 0,1158" fill="var(--navy-deep)"/>
    <rect x="0" y="1166" width="970" height="34" fill="var(--blue-light)"/>

    <!-- pathway badges -->
    <g class="badge badge-education">
      <circle cx="136" cy="803" r="88" fill="var(--ring)"/>
      <circle cx="136" cy="803" r="80" fill="var(--blue)"/>
      <polygon points="136,765 198,788 136,811 74,788" fill="#fff"/>
      <path d="M102,800 v22 q34,16 68,0 v-22 l-34,13 z" fill="#fff"/>
      <line x1="190" y1="791" x2="190" y2="830" stroke="#fff" stroke-width="3"/>
      <rect x="186" y="828" width="8" height="14" fill="#fff"/>
    </g>
    <g class="badge badge-computing">
      <circle cx="377" cy="747" r="88" fill="var(--ring)"/>
      <circle cx="377" cy="747" r="80" fill="var(--blue)"/>
      <rect x="362" y="735" width="60" height="38" rx="3" fill="none" stroke="#fff" stroke-width="6"/>
      <rect x="350" y="776" width="84" height="7" rx="2" fill="#fff"/>
      <circle cx="365" cy="722" r="13" fill="none" stroke="#fff" stroke-width="9" stroke-dasharray="5 3.2"/>
      <circle cx="365" cy="722" r="9" fill="none" stroke="#fff" stroke-width="5"/>
      <circle cx="336" cy="748" r="9" fill="none" stroke="#fff" stroke-width="7" stroke-dasharray="4 2.6"/>
      <circle cx="336" cy="748" r="6" fill="none" stroke="#fff" stroke-width="4"/>
    </g>
    <g class="badge badge-engineering">
      <circle cx="601" cy="666" r="88" fill="var(--ring)"/>
      <circle cx="601" cy="666" r="80" fill="var(--blue)"/>
      <circle cx="592" cy="668" r="28" fill="none" stroke="#fff" stroke-width="14" stroke-dasharray="9 5.5"/>
      <circle cx="592" cy="668" r="24" fill="none" stroke="#fff" stroke-width="10"/>
      <ellipse cx="606" cy="662" rx="40" ry="14" fill="none" stroke="#fff" stroke-width="3" transform="rotate(-30 606 662)"/>
      <ellipse cx="606" cy="662" rx="40" ry="14" fill="none" stroke="#fff" stroke-width="3" transform="rotate(40 606 662)"/>
      <circle cx="606" cy="662" r="6" fill="#fff"/>
    </g>
    <g class="badge badge-health">
      <circle cx="837" cy="578" r="88" fill="var(--ring)"/>
      <circle cx="837" cy="578" r="80" fill="var(--blue)"/>
      <rect x="826" y="536" width="22" height="84" rx="3" fill="#fff"/>
      <rect x="795" y="567" width="84" height="22" rx="3" fill="#fff"/>
    </g>

    <!-- contact tab -->
    <polygon points="562,903 970,903 970,952 536,952" fill="var(--blue)"/>
  </svg>

  <div class="abs brand-row">
    <div class="brand"><span class="brand-mark"></span>Birchvale Public Schools</div>
    <div class="brand"><span class="brand-mark"></span>Ridgewater Technical College</div>
  </div>

  <h1 class="abs program-title">BVA Early College<br>Program</h1>
  <p class="abs program-lead">Earn credit for both High School and College and Learn more about the career focused courses in</p>

  <section class="abs perks">
    <h2>THINGS TO LOOK FORWARD TO:</h2>
    <ul>
      <li>Experience college in high school</li>
      <li>Finish college early</li>
      <li>Save money on college tuition and fees</li>
      <li>Get advice on your future career</li>
    </ul>
  </section>

  <div class="abs pathway-label" style="left:136px;top:898px">EDUCATION</div>
  <div class="abs pathway-label" style="left:377px;top:843px">COMPUTER &amp;<br>INFORMATION SCIENCE</div>
  <div class="abs pathway-label" style="left:601px;top:761px">TECHNOLOGY &amp;<br>ENGINEERING</div>
  <div class="abs pathway-label" style="left:837px;top:674px">HEALTH</div>

  <div class="abs cta-text">FOR MORE INFORMATION CONTACT</div>

  <div class="abs contact" style="left:51px">
    <h3>Peter Hollis</h3>
    <p>PK12 Partnerships -RWTC</p>
    <p><svg width="14" height="14" viewBox="0 0 24 24"><path d="M6.6 10.8a15 15 0 0 0 6.6 6.6l2.2-2.2a1 1 0 0 1 1-.25 11.4 11.4 0 0 0 3.6.57 1 1 0 0 1 1 1V20a1 1 0 0 1-1 1A17 17 0 0 1 3 4a1 1 0 0 1 1-1h3.5a1 1 0 0 1 1 1c0 1.25.2 2.45.57 3.57a1 1 0 0 1-.25 1z" fill="var(--blue-light)"/></svg>555.204.3189</p>
    <p class="mail"><svg width="14" height="10" viewBox="0 0 14 10"><rect width="14" height="10" fill="var(--blue-light)"/><path d="M0 0l7 6 7-6" fill="none" stroke="var(--navy-deep)" stroke-width="1.3"/></svg>phollis@rwtc.example.edu</p>
  </div>

  <div class="abs contact" style="left:322px">
    <h3>Ms. Delgany</h3>
    <p>Early College Coordinator</p>
    <p>Room K215</p>
    <p class="mail"><svg width="14" height="10" viewBox="0 0 14 10"><rect width="14" height="10" fill="var(--blue-light)"/><path d="M0 0l7 6 7-6" fill="none" stroke="var(--navy-deep)" stroke-width="1.3"/></svg>marta.delgany@birchvale.example.org</p>
  </div>

  <div class="abs contact" style="left:650px">
    <h3>Ms. Okafor</h3>
    <p>Work-Based Learning Coordinator</p>
    <p>Room K215</p>
    <p class="mail"><svg width="14" height="10" viewBox="0 0 14 10"><rect width="14" height="10" fill="var(--blue-light)"/><path d="M0 0l7 6 7-6" fill="none" stroke="var(--navy-deep)" stroke-width="1.3"/></svg>nadia.okafor@birchvale.example.org</p>
  </div>
</main>
</body>
</html>
```